Certified Public Accountant specializing in tax preparation.

I need a business card designed that conveys knowledgeability, trustworthiness and competency. I am a licensed CPA and hold a Master's in taxation. As this is a personal service business, I would like to include my picture on the card.

```html
<!DOCTYPE html>
<html lang="en">
<head>
<meta charset="utf-8">
<title>Clara Jane Morrow – Business Card</title>
<link href="https://fonts.googleapis.com/css2?family=Fredoka:wght@500&family=Lato:wght@400;700&display=swap" rel="stylesheet">
<style>
  :root {
    --backdrop: #3b3b3d;
    --card: #ffffff;
    --brand-pink: #ec2a7a;
    --charcoal: #2e2e33;
    --steel: #8a8a8e;
    --ink: #2b2b2b;
    --photo-light: #ead7d6;
    --photo-mid: #d7a9b9;
    --photo-dark: #5a3a2e;
  }
  html, body {
    margin: 0;
    width: 1200px;
    height: 899px;
    overflow: hidden;
    background: var(--backdrop);
  }
  .stage {
    position: relative;
    width: 1200px;
    height: 899px;
  }
  .card {
    position: absolute;
    left: 250px;
    width: 700px;
    height: 400px;
    filter: drop-shadow(0 10px 18px rgba(0,0,0,.45));
  }
  .card--front { top: 38px; }
  .card--back  { top: 462px; }
  .name {
    font-family: "Fredoka", "Baloo 2", sans-serif;
    font-weight: 500;
    font-size: 38px;
    fill: var(--brand-pink);
  }
  .title {
    font-family: "Lato", sans-serif;
    font-size: 17px;
    fill: var(--ink);
    letter-spacing: .5px;
  }
  .contact {
    font-family: "Lato", sans-serif;
    font-size: 16px;
    fill: var(--ink);
  }
  .contact--light { fill: #ffffff; }
  .web-light {
    font-family: "Lato", sans-serif;
    font-size: 16px;
    fill: #ffffff;
  }
  .icon { fill: var(--brand-pink); }
  .icon--light { fill: #ffffff; }
</style>
</head>
<body>
<div class="stage">

  <!-- Card one -->
  <svg class="card card--front" viewBox="0 0 700 400" xmlns="http://www.w3.org/2000/svg">
    <defs>
      <clipPath id="front-shape"><rect width="700" height="400" rx="30"/></clipPath>
      <linearGradient id="portrait-tone-a" x1="0" y1="0" x2="0" y2="1">
        <stop offset="0" stop-color="var(--photo-dark)"/>
        <stop offset=".45" stop-color="var(--photo-light)"/>
        <stop offset="1" stop-color="var(--photo-mid)"/>
      </linearGradient>
    </defs>
    <g clip-path="url(#front-shape)">
      <rect class="card-base" width="700" height="400" fill="var(--card)"/>
      <path class="top-tab" d="M0 0 H262 Q272 0 272 10 V24 H0 Z" fill="var(--charcoal)"/>
      <rect class="top-band" x="280" y="0" width="420" height="24" fill="var(--brand-pink)"/>
      <rect class="portrait" role="img" aria-label="Portrait photo of the accountant in a pink blazer" x="450" y="44" width="230" height="356" rx="6" fill="url(#portrait-tone-a)"/>
    </g>
    <text class="name" x="58" y="212">Clara Jane Morrow</text>
    <text class="title" x="60" y="242">Licensed CPA  |  Master's in taxation</text>

    <text class="contact" x="60" y="286">48 Harbor Lane, Suite B</text>
    <text class="contact" x="60" y="308">Leeds, UK LS12 4QB</text>

    <path class="icon" d="M62 325 q-2 8 6 14 l3 -3 -4 -4 -2 2 q-3 -3 -2 -6 l2 -1 -2 -4 z"/>
    <text class="contact" x="84" y="338">020 555 0184</text>

    <rect class="icon" x="61" y="350" width="14" height="10" rx="1"/>
    <path d="M61 351 l7 5 7 -5" fill="none" stroke="#fff" stroke-width="1.4"/>
    <text class="contact" x="84" y="360">clara.morrow@mailbox.com</text>

    <circle class="icon" cx="68" cy="377" r="7"/>
    <path d="M61 377 h14 M68 370 v14" stroke="#fff" stroke-width="1.2"/>
    <text class="contact" x="84" y="382">www.claramorrow.com</text>
  </svg>

  <!-- Card two -->
  <svg class="card card--back" viewBox="0 0 700 400" xmlns="http://www.w3.org/2000/svg">
    <defs>
      <clipPath id="back-shape"><rect width="700" height="400" rx="30"/></clipPath>
      <linearGradient id="portrait-tone-b" x1="0" y1="0" x2="0" y2="1">
        <stop offset="0" stop-color="var(--photo-dark)"/>
        <stop offset=".5" stop-color="var(--photo-light)"/>
        <stop offset="1" stop-color="var(--photo-mid)"/>
      </linearGradient>
    </defs>
    <g clip-path="url(#back-shape)">
      <rect class="card-base" width="700" height="400" fill="var(--card)"/>
      <rect class="portrait" role="img" aria-label="Portrait photo of the accountant in a pink blazer" x="450" y="18" width="220" height="230" rx="6" fill="url(#portrait-tone-b)"/>
      <path class="wave-accent" d="M0 284 C200 252 440 232 700 118 L700 140 C440 254 200 274 0 306 Z" fill="var(--steel)"/>
      <path class="wave-shadow" d="M0 296 C200 264 440 244 700 130 L700 400 L0 400 Z" fill="var(--charcoal)"/>
      <path class="wave-band" d="M0 306 C200 274 440 254 700 140 L700 400 L0 400 Z" fill="var(--brand-pink)"/>
    </g>
    <text class="name" x="58" y="164">Clara Jane Morrow</text>
    <text class="title" x="60" y="194">Licensed CPA  |  Master's in taxation</text>

    <text class="web-light" x="672" y="236" text-anchor="end">www.claramorrow.com</text>

    <line x1="48" y1="312" x2="48" y2="394" stroke="#fff" stroke-width="2"/>
    <text class="contact contact--light" x="66" y="326">48 Harbor Lane, Suite B</text>
    <text class="contact contact--light" x="66" y="347">Leeds, UK LS12 4QB</text>

    <path class="icon--light" d="M68 357 q-2 8 6 14 l3 -3 -4 -4 -2 2 q-3 -3 -2 -6 l2 -1 -2 -4 z"/>
    <text class="contact contact--light" x="90" y="369">020 555 0184</text>

    <rect class="icon--light" x="67" y="380" width="14" height="10" rx="1"/>
    <path d="M67 381 l7 5 7 -5" fill="none" stroke="var(--brand-pink)" stroke-width="1.4"/>
    <text class="contact contact--light" x="90" y="390">clara.morrow@mailbox.com</text>
  </svg>

</div>
</body>
</html>
```